VarnLink Signal Systems Website Design

We are an Australian based telecommunications company who specialise in the design, build and implementation of mission critical communications infrastructure. We have offices throughout Australia, New Zealand and Europe. Our Customers are operators in multiple markets from Oil & Gas, Mining, Government, Utilities, Carrier & Transportation.

We also work with large multi-national companies, that provide telecommunication and services such as; Pelvaro, Dransvik, Quorba, Talmoss and many more. We want to be able to achieve the same level of impressions and professionalism as what these companies present on their websites.

To reflect our recent move into the European market, we need our new site to reflect who we are as a company, and exhibit the fact we are not just based in Australia, but we are a global organisation. We want to have a fresh clean look, thats modern, dynamic and simple. Flat textures and colours are perfect for us to adapt to. A site that is based around content management, with a responsive design that can be used on all devices.

We have started to develop a basic design language that we would like to incorporate in our overall website design. We have attached some documents that highlight our design language and we can provide colour codes and fonts to ensure consistency.

Our existing site is: www.varnlinkss.example. Please feel free to view and pick apart items. From this example, we would massive improvement in how the site looks, feels and functions. We also want social media to form a big part of our site, with the likes of posts from chirpnet and blogs posting capabilities.

If you require anymore information about VarnLink or our requirements, please do not hesitate to contact.

Thanks and good luck!

Target Market(s)

Potential & Existing Customers, New international customers & markets, New Market Sectors, Partners, Service Providers

Industry/Entity Type

Telecommunications

Coding

Coded - Design and coding required

Number of Pages Required

5+ page

Font styles to use
Sans Serif

Requirements
Must have
• Content Management, Responsive Design for multiple device compatibility, Social media integration, use of lots of imagery, drop down menus, search capabilities
Should not have
• No flash.

```html
<!DOCTYPE html>
<html lang="en">
<head>
<meta charset="utf-8">
<title>VarnLink Signal Systems</title>
<link href="https://fonts.googleapis.com/css2?family=Roboto:wght@300;400;500;700&display=swap" rel="stylesheet">
<style>
:root{
  --navy:#1f3461;
  --navy-deep:#172a52;
  --ink:#333a44;
  --muted:#8a8f98;
  --soft:#efefef;
  --line:#d9dbe0;
  --white:#ffffff;
  --sky-1:#2b5aa6;
  --sky-2:#6f95cf;
  --award-orange:#f0831f;
  --award-blue:#2a6fb5;
}
*{margin:0;padding:0;box-sizing:border-box}
html,body{width:1200px;height:2778px;overflow:hidden}
body{font-family:'Roboto',Arial,sans-serif;color:var(--ink);background:var(--white);position:relative}
.wrap{position:absolute;left:78px;width:1044px}
a{color:inherit;text-decoration:none}

/* top bar */
.topbar{position:absolute;top:0;left:0;width:1200px;height:52px;border-bottom:1px solid #e6e6e6}
.contact{position:absolute;left:78px;top:16px;font-size:15px;color:var(--muted);display:flex;gap:26px;align-items:center}
.contact span{display:flex;align-items:center;gap:8px}
.social-top{position:absolute;left:730px;top:8px;display:flex;gap:8px}
.dot{width:36px;height:36px;border-radius:50%;background:#b9bcc2}
.dot.first{background:var(--navy)}
.search{position:absolute;left:903px;top:9px;width:219px;height:36px;border:1px solid var(--line);background:#f6f6f6;font-size:14px;color:var(--muted);padding:9px 12px}
.search svg{position:absolute;right:10px;top:8px}

/* header */
.header{position:absolute;top:52px;left:0;width:1200px;height:105px}
.brand{position:absolute;left:78px;top:32px;display:flex;align-items:center;gap:10px;color:var(--navy);font-size:34px;font-weight:700}
.brand .mark{width:16px;height:16px;border-radius:50%;background:var(--navy)}
.nav{position:absolute;left:363px;top:29px;display:flex;align-items:center;gap:30px;font-size:16px;color:#6b7079;letter-spacing:.3px}
.nav .home{background:var(--navy);color:var(--white);border-radius:25px;padding:15px 24px;font-weight:500}

/* hero */
.hero{position:absolute;top:157px;left:0;width:1200px;height:500px}
.hero-photo{position:absolute;inset:0;background:linear-gradient(100deg,var(--sky-1) 0%,#3a68b2 45%,var(--sky-2) 100%)}
.hero h1{position:absolute;left:78px;top:126px;font-size:54px;line-height:58px;font-weight:500;color:var(--white);letter-spacing:.5px}
.hero p{position:absolute;left:78px;top:250px;width:500px;font-size:18px;line-height:27px;color:var(--white)}
.btn{position:absolute;left:78px;top:323px;width:219px;height:56px;border:2px solid var(--white);border-radius:30px;background:var(--navy);color:var(--white);font-size:18px;font-weight:500;display:flex;align-items:center;justify-content:center}

/* services */
.services{position:absolute;top:657px;left:0;width:1200px;height:519px}
.section-title{font-size:40px;font-weight:300;text-align:center;letter-spacing:.5px;color:#4a4f58}
.section-title b{font-weight:400;color:var(--navy)}
.services .section-title{position:absolute;top:60px;width:1200px}
.lead{font-size:16px;line-height:25px;color:var(--muted);text-align:center}
.services .lead{position:absolute;top:118px;left:300px;width:600px}
.svc-row{position:absolute;top:190px;left:78px;width:1044px;display:grid;grid-template-columns:repeat(6,1fr)}
.svc{text-align:center}
.svc-icon{width:118px;height:118px;margin:0 auto;border-radius:50%;background:#f3f3f3;box-shadow:inset 10px 0 0 var(--navy);display:flex;align-items:center;justify-content:center}
.svc h3{margin-top:22px;font-size:18px;line-height:23px;font-weight:400;color:var(--ink)}
.svc p{margin:12px auto 0;width:150px;font-size:13px;line-height:25px;color:var(--muted)}

/* welcome */
.welcome{position:absolute;top:1176px;left:0;width:1200px;height:389px;background:var(--soft)}
.welcome h2{position:absolute;left:78px;top:62px;font-size:38px;font-weight:300;color:#3b4048}
.welcome h2 b{font-weight:400;color:var(--navy)}
.welcome .intro{position:absolute;left:78px;top:118px;width:640px;font-size:14px;line-height:27px;color:var(--muted)}
.divider{position:absolute;left:737px;top:68px;width:1px;height:250px;background:var(--line)}
.feature{position:absolute;top:222px;width:310px;display:flex;gap:14px}
.feature .ic{flex:none;width:104px;height:104px;border-radius:50%;background:var(--white);box-shadow:inset 9px 0 0 var(--navy);display:flex;align-items:center;justify-content:center}
.feature h4{font-size:19px;font-weight:400;color:var(--navy);margin-top:8px}
.feature p{font-size:13.5px;line-height:21px;color:var(--muted);margin-top:6px}
.welcome-brand{position:absolute;left:790px;top:160px;display:flex;align-items:center;gap:14px;color:var(--navy);font-size:56px;font-weight:700}
.welcome-brand .mark{width:24px;height:24px;border-radius:50%;background:var(--navy)}

/* market */
.market{position:absolute;top:1565px;left:0;width:1200px;height:482px;background:var(--navy)}
.market .section-title{position:absolute;top:60px;width:1200px;color:var(--white);font-weight:400}
.market .lead{position:absolute;top:114px;left:250px;width:700px;color:#dde3ee}
.cards{position:absolute;top:185px;left:78px;width:1044px;display:grid;grid-template-columns:repeat(4,1fr);gap:15px}
.card-photo{height:166px}
.card-photo.oil{background:linear-gradient(180deg,#5c86b8,#8a7a5a)}
.card-photo.mining{background:linear-gradient(180deg,#9fb3c9,#a98a62)}
.card-photo.carrier{background:linear-gradient(180deg,#2c5ca8,#4a78c0)}
.card-photo.transport{background:linear-gradient(180deg,#b9c3cf,#8a8f94)}
.card-label{height:52px;background:#f2f2f2;font-size:19px;color:var(--ink);display:flex;align-items:center;justify-content:center}
.pager{position:absolute;top:420px;left:563px;display:flex;gap:10px}
.pager i{display:block;width:30px;height:3px;background:#6f80a3}
.pager i.on{background:var(--white)}

/* support */
.support{position:absolute;top:2047px;left:0;width:1200px;height:283px}
.support h2{position:absolute;left:78px;top:60px;font-size:38px;font-weight:300;color:#3b4048}
.support h2 b{font-weight:400;color:var(--navy)}
.support p{position:absolute;left:78px;top:118px;width:640px;font-size:14px;line-height:27px;color:var(--muted)}
.award{position:absolute;top:58px;width:150px;text-align:center}
.badge{margin:0 auto;width:90px;height:80px}
.badge.round{border-radius:50%;background:var(--award-orange)}
.badge.square{width:62px;height:72px;background:var(--award-blue)}
.award span{display:block;margin-top:16px;font-size:13px;line-height:22px;color:var(--muted)}

/* partners */
.partners{position:absolute;top:2330px;left:0;width:1200px;height:142px;background:var(--soft);display:flex;align-items:center;justify-content:space-around;padding:0 78px}
.partners span{font-size:44px;font-weight:500;color:#2b2f36;letter-spacing:1px}

/* footer */
.footer{position:absolute;top:2472px;left:0;width:1200px;height:241px;background:var(--navy);color:#dfe5ef}
.footer .brand{top:70px;color:var(--white);font-size:34px}
.footer .brand .mark{background:var(--white)}
.links{position:absolute;top:44px;display:flex;flex-direction:column;gap:7px;font-size:14.5px;line-height:20px}
.bottom{position:absolute;top:2713px;left:0;width:1200px;height:65px;background:var(--navy-deep);color:#e6ebf3;font-size:14px}
.bottom .copy{position:absolute;left:78px;top:24px}
.bottom .connect{position:absolute;right:78px;top:17px;display:flex;align-items:center;gap:14px}
.bottom .connect i{display:block;width:20px;height:20px;border-radius:50%;background:#cfd7e6}
</style>
</head>
<body>

<div class="topbar">
  <div class="contact">
    <span><svg width="16" height="16" viewBox="0 0 24 24" fill="#1f3461"><path d="M6.6 10.8a15 15 0 006.6 6.6l2.2-2.2c.3-.3.7-.4 1-.2 1.1.4 2.3.6 3.6.6.6 0 1 .4 1 1V20c0 .6-.4 1-1 1A17 17 0 013 4c0-.6.4-1 1-1h3.5c.6 0 1 .4 1 1 0 1.3.2 2.5.6 3.6.1.3 0 .7-.2 1z"/></svg>+44 170 555 0182</span>
    <span><svg width="18" height="14" viewBox="0 0 24 18" fill="none" stroke="#1f3461" stroke-width="2"><rect x="1" y="1" width="22" height="16" rx="1"/><path d="M1 2l11 8 11-8"/></svg>info@varnlinkss.example</span>
  </div>
  <div class="social-top"><i class="dot first"></i><i class="dot"></i><i class="dot"></i><i class="dot"></i></div>
  <div class="search">Search..
    <svg width="20" height="20" viewBox="0 0 24 24" fill="none" stroke="#8a8f98" stroke-width="2.4"><circle cx="10" cy="10" r="7"/><path d="M15 15l7 7"/></svg>
  </div>
</div>

<header class="header">
  <div class="brand"><i class="mark"></i>VarnLink</div>
  <nav class="nav">
    <a class="home">HOME</a><a>PRODUCTS &amp; SERVICES</a><a>SECTORS</a><a>SUPPORT</a><a>CORPORATE</a><a>CONTACT</a>
  </nav>
</header>

<section class="hero">
  <div class="hero-photo" role="img" aria-label="Telecommunications lattice tower with antennas against a blue sky"></div>
  <h1>WHATEVER THE<br>ENVIRONMENT</h1>
  <p>Quickly deploy communications infrastructure in the most demanding conditions with our rapid site solution</p>
  <a class="btn">KNOW MORE</a>
</section>

<section class="services">
  <h2 class="section-title">OUR BUSINESS <b>SERVICES</b></h2>
  <p class="lead">VarnLink's core businesses are structured into functional teams, each offering a varied selection of products and services</p>
  <div class="svc-row">
    <div class="svc">
      <div class="svc-icon"><svg width="50" height="50" viewBox="0 0 48 48" fill="none" stroke="#1f3461" stroke-width="2.5"><path d="M6 28h36v10H6z"/><path d="M14 28l10-14 10 14"/><path d="M20 20h8"/></svg></div>
      <h3>Supply &amp; Solution Development</h3>
      <p>The supply &amp; Solutions Development team is responsible for the</p>
    </div>
    <div class="svc">
      <div class="svc-icon"><svg width="50" height="50" viewBox="0 0 48 48" fill="none" stroke="#1f3461" stroke-width="2.5"><path d="M24 20v22M18 42l6-22 6 22"/><circle cx="24" cy="17" r="3"/><path d="M16 10a11 11 0 000 14M32 10a11 11 0 010 14M11 6a17 17 0 000 22M37 6a17 17 0 010 22"/></svg></div>
      <h3>Rapid Site Solution</h3>
      <p>The Rapid Site Solution(RSS) team provides a unique.</p>
    </div>
    <div class="svc">
      <div class="svc-icon"><svg width="50" height="50" viewBox="0 0 48 48" fill="none" stroke="#1f3461" stroke-width="2.5"><rect x="7" y="7" width="34" height="34" rx="3"/><path d="M13 17h22M13 24h22M13 31h22"/><circle cx="19" cy="17" r="2.5" fill="#fff"/><circle cx="29" cy="24" r="2.5" fill="#fff"/><circle cx="22" cy="31" r="2.5" fill="#fff"/></svg></div>
      <h3>Operational Support systems</h3>
      <p>The Operational Support Systems (OSS) team is a specialist.</p>
    </div>
    <div class="svc">
      <div class="svc-icon"><svg width="50" height="50" viewBox="0 0 48 48" fill="none" stroke="#1f3461" stroke-width="2.5"><circle cx="24" cy="24" r="15"/><circle cx="24" cy="9" r="3.5" fill="#fff"/><circle cx="11" cy="31" r="3.5" fill="#fff"/><circle cx="37" cy="31" r="3.5" fill="#fff"/><path d="M24 12v12l-10 6M24 24l10 6"/></svg></div>
      <h3>Professional Services</h3>
      <p>The Professional Services team are responsibe for.</p>
    </div>
    <div class="svc">
      <div class="svc-icon"><svg width="50" height="50" viewBox="0 0 48 48" fill="none" stroke="#1f3461" stroke-width="2.5"><circle cx="24" cy="21" r="9"/><path d="M11 24v-4a13 13 0 0126 0v4"/><rect x="8" y="20" width="5" height="9" rx="2"/><rect x="35" y="20" width="5" height="9" rx="2"/><path d="M37 29c0 6-5 9-11 9"/><path d="M12 44c2-6 7-8 12-8s10 2 12 8"/></svg></div>
      <h3>After Sales Support</h3>
      <p>The After Sales Support team offers flexible.</p>
    </div>
    <div class="svc">
      <div class="svc-icon"><svg width="50" height="50" viewBox="0 0 48 48" fill="none" stroke="#1f3461" stroke-width="2.5"><rect x="6" y="7" width="28" height="22" rx="1"/><circle cx="36" cy="18" r="4"/><path d="M31 44V28h10v16M36 28v16M20 29v8"/></svg></div>
      <h3>Training</h3>
      <p>The Training team provides and delivers an ecxtensive</p>
    </div>
  </div>
</section>

<section class="welcome">
  <h2>WELCOME TO <b>VARNLINK</b></h2>
  <p class="intro">In 1998, the Directors identified the need for a specialist value added reseller that could provide quality communications systems and services that were more appropriate and better suited to mission critical and industrial applications.</p>
  <div class="feature" style="left:78px">
    <div class="ic"><svg width="46" height="46" viewBox="0 0 48 48" fill="none" stroke="#7f8fae" stroke-width="3"><circle cx="22" cy="26" r="16"/><circle cx="22" cy="26" r="9"/><circle cx="22" cy="26" r="2.5" fill="#7f8fae"/><path d="M22 26L40 8M34 8h6v6"/></svg></div>
    <div><h4>Our Mission</h4><p>To be a leading international provider of advanced and engineered...</p></div>
  </div>
  <div class="feature" style="left:402px">
    <div class="ic"><svg width="50" height="46" viewBox="0 0 52 48" fill="none" stroke="#7f8fae" stroke-width="3"><path d="M2 18l10-6 8 4 8-4 10 4 12-2"/><path d="M12 30l10 10c2 2 5 2 6 0l12-12-10-10-8 6"/><path d="M2 18l10 12M50 14l-10 14"/></svg></div>
    <div><h4>Our Value</h4><p>The VarnLink Way describes how we work as a team and how we interact..</p></div>
  </div>
  <div class="divider"></div>
  <div class="welcome-brand"><i class="mark"></i>VarnLink</div>
</section>

<section class="market">
  <h2 class="section-title">MARKET SECTOR</h2>
  <p class="lead">VarnLink specialises in design and development of systems and networks that meet the stringent requirements of mission-critical industries.</p>
  <div class="cards">
    <div><div class="card-photo oil" role="img" aria-label="Oil and gas processing plant"></div><div class="card-label">Oil &amp; Gas</div></div>
    <div><div class="card-photo mining" role="img" aria-label="Haul truck at an open-cut mine"></div><div class="card-label">Mining</div></div>
    <div><div class="card-photo carrier" role="img" aria-label="Carrier communications tower"></div><div class="card-label">Carrier</div></div>
    <div><div class="card-photo transport" role="img" aria-label="Passenger train at a station platform"></div><div class="card-label">Transport</div></div>
  </div>
  <div class="pager"><i></i><i class="on"></i></div>
</section>

<section class="support">
  <h2>TECHNICAL <b>SUPPORT</b></h2>
  <p>VarnLink offers flexible multi-technology and multi-vendor support services. We take an end-to-end view of networks, helping you to resolve issues quickly and completely. Our unparalleled expertise in building and supporting critical communications infrastructure gives VarnLink the experience to solve your network problem</p>
  <div class="award" style="left:790px"><div class="badge round"></div><span>2003 - Business Fast<br>100 Companies Award</span></div>
  <div class="award" style="left:968px"><div class="badge square"></div><span>2009 - Import/Export<br>Wholesale Award</span></div>
</section>

<section class="partners">
  <span>Quorba</span><span>Talmoss</span><span>Kestavo</span><span>Brindlex</span>
</section>

<footer class="footer">
  <div class="brand"><i class="mark"></i>VarnLink</div>
  <div class="links" style="left:344px"><a>Partners &amp; Technology</a><a>Industries</a><a>Professional Services</a><a>Case studies</a><a>Support</a><a>Corporate</a></div>
  <div class="links" style="left:609px"><a>Rapid site Solution</a><a>OSS</a><a>Responsibilities</a><a>Contact</a></div>
  <div class="links" style="left:874px"><a>Legal Information</a><a>Privacy Policy</a><a>Terms of Use</a><a>Cookies</a><a>Site map</a></div>
</footer>

<div class="bottom">
  <div class="copy">©VarnLink Signal Systems - 2016. All Rights Reserved.</div>
  <div class="connect">Connect with us :<i></i><i></i><i></i><i></i></div>
</div>

</body>
</html>
```